Design for a Note buying company that attracts landlords and seller financed notes

I need a card designed. I want a simple clean front with my logo and contact info. On the back I want some big and bold words to get a message across.

Our Company buys Notes (mortgages) and we want to convey the sense of financial security. Our number one market that we pursue is tired landlords.

If you want to understand our business you can visit our website. www.lakeviewpaperfund.com

Do not use any Clip Art in the design, it will not be accepted. I want a custom designed card not something I could throw together myself. Simple clean and drive the message home.

Target Market(s)

Landlords, seller financed note holders

Industry/Entity Type

Mortgage

Contact Information for Business Card

Simple clean and bold. I need to grab the attention of the customer. It should convey a professional touch.

Font styles to use
Sans Serif

Colors
ec2229
ffffff

Requirements
Must have
• Clean front with logo and contact information
Front colors should match logo

Back should be bold and grab attention. Back colors are open to ideas
Nice to have
• The Back May use the phrase "No more Tentants, No more Toilets" "More Time, More Cash"

I'm open to other ideas about grabbing a landlords attention

I'm open to a square card design
I like cards with round corners as well
Should not have
• any clip art! must be custom designs.

```html
<!DOCTYPE html>
<html lang="en">
<head>
<meta charset="utf-8">
<title>Lakeview Note Buyers – Business Card</title>
<link href="https://fonts.googleapis.com/css2?family=Montserrat:wght@500;700;800&family=Roboto:wght@400;500&family=Playfair+Display:wght@900&display=swap" rel="stylesheet">
<style>
  :root {
    --brand-red: #ec2229;
    --ink: #111111;
    --paper: #ffffff;
    --stage: #e9eaec;
    --muted: #333333;
  }
  * { box-sizing: border-box; margin: 0; padding: 0; }
  html, body { width: 1200px; height: 800px; overflow: hidden; background: var(--stage); }
  .sheet {
    width: 1200px; height: 800px;
    display: flex; align-items: center; justify-content: center; gap: 40px;
  }
  .card {
    width: 560px; height: 320px; position: relative; overflow: hidden;
    box-shadow: 0 10px 24px rgba(0,0,0,.12);
  }

  /* Front */
  .card--front { background: var(--paper); font-family: "Roboto", sans-serif; }
  .brand {
    position: absolute; left: 40px; top: 88px; width: 210px;
    display: flex; align-items: center; gap: 12px;
  }
  .brand__mark { width: 22px; height: 22px; background: var(--brand-red); flex: none; }
  .brand__name {
    font-family: "Montserrat", sans-serif; font-weight: 800; font-size: 21px;
    line-height: 1.1; color: var(--ink); text-transform: uppercase; letter-spacing: .5px;
  }
  .divider {
    position: absolute; left: 268px; top: 54px; width: 1px; height: 150px; background: var(--muted);
  }
  .contact { position: absolute; left: 290px; top: 58px; }
  .contact__name {
    font-family: "Montserrat", sans-serif; font-weight: 700; font-size: 17px;
    color: var(--ink); text-transform: uppercase; letter-spacing: .3px;
  }
  .contact__role {
    font-family: "Montserrat", sans-serif; font-weight: 700; font-size: 13px;
    color: var(--brand-red); margin: 2px 0 10px;
  }
  .contact__list { list-style: none; }
  .contact__item {
    display: flex; align-items: center; gap: 7px;
    font-size: 13px; color: var(--ink); line-height: 20px;
  }
  .contact__icon { width: 11px; height: 11px; flex: none; fill: var(--brand-red); }
  .address-band {
    position: absolute; left: 0; right: 0; top: 232px; height: 34px; background: var(--ink);
    display: flex; align-items: center; justify-content: flex-end; padding-right: 78px;
  }
  .address-band__text { color: var(--paper); font-size: 13px; letter-spacing: .3px; }
  .address-band__square {
    position: absolute; right: 22px; top: -14px; width: 44px; height: 44px; background: var(--brand-red);
  }

  /* Back */
  .card--back { background: var(--ink); }
  .slogan {
    position: absolute; left: 50%; top: 50%; transform: translate(-50%, -50%);
    width: 440px; text-align: center;
  }
  .slogan__rule { height: 2px; background: var(--brand-red); width: 300px; }
  .slogan__rule--top { margin-left: auto; }
  .slogan__rule--bottom { margin-right: auto; }
  .slogan__body { position: relative; padding: 16px 44px; }
  .slogan__text {
    font-family: "Playfair Display", serif; font-weight: 900; font-size: 24px;
    line-height: 1.25; color: var(--paper); text-transform: uppercase; letter-spacing: .5px;
  }
  .slogan__quote {
    position: absolute; font-family: "Playfair Display", serif; font-weight: 900;
    font-size: 52px; line-height: 1; color: var(--brand-red);
  }
  .slogan__quote--open { left: 0; top: 40px; }
  .slogan__quote--close { right: 0; top: 8px; }
</style>
</head>
<body>
<main class="sheet">
  <section class="card card--front" aria-label="Card front">
    <div class="brand">
      <span class="brand__mark"></span>
      <span class="brand__name">Lakeview<br>Note Buyers</span>
    </div>
    <div class="divider"></div>
    <div class="contact">
      <p class="contact__name">Dana Whitlock</p>
      <p class="contact__role">Founder</p>
      <ul class="contact__list">
        <li class="contact__item">
          <svg class="contact__icon" viewBox="0 0 12 12"><rect x="3" y="0" width="6" height="12" rx="1"/><rect x="4" y="1.5" width="4" height="8" fill="#fff"/></svg>
          555.201.4478</li>
        <li class="contact__item">
          <svg class="contact__icon" viewBox="0 0 12 12"><path d="M1 4c0-2 2-3 5-3s5 1 5 3l-2 1-1-1H4L3 5z"/><rect x="2" y="6" width="8" height="5" rx="1"/></svg>
          555.340.6612</li>
        <li class="contact__item">
          <svg class="contact__icon" viewBox="0 0 12 12"><rect x="0" y="2" width="12" height="8"/><path d="M0 2l6 5 6-5" fill="none" stroke="#fff" stroke-width="1.2"/></svg>
          info@lakeviewpaperfund.com</li>
        <li class="contact__item">
          <svg class="contact__icon" viewBox="0 0 12 12"><circle cx="6" cy="6" r="6"/><path d="M0 6h12M6 0c-3 3-3 9 0 12M6 0c3 3 3 9 0 12" fill="none" stroke="#fff" stroke-width="1"/></svg>
          www.lakeviewpaperfund.com</li>
      </ul>
    </div>
    <div class="address-band">
      <span class="address-band__text">P.O. Box 19 Millbrook, Kansas 67500</span>
      <span class="address-band__square"></span>
    </div>
  </section>

  <section class="card card--back" aria-label="Card back">
    <div class="slogan">
      <div class="slogan__rule slogan__rule--top"></div>
      <div class="slogan__body">
        <span class="slogan__quote slogan__quote--open">&ldquo;</span>
        <p class="slogan__text">Sell your note,<br>skip the repairs<br>keep your weekends</p>
        <span class="slogan__quote slogan__quote--close">&rdquo;</span>
      </div>
      <div class="slogan__rule slogan__rule--bottom"></div>
    </div>
  </section>
</main>
</body>
</html>
```